Blog Banner Design Project: Notes For Wanderers

Looking for a new banner for my blog " Colin Ashworth's Notes for Wanderers" at http://www.notesforwanderers.example - and once design agreed also want an updated album art for the podcast that goes along with the site.
For more about the blog and what it is about:
http://www.notesforwanderers.example/about
Notes for Wanderers is a Luxury Travel Blog And Podcast that provides inspiration, advice and tips about luxurious travel experiences, including destinations, transportation, accommodation, and journeys, that travellers can read, listen to or watch.
Objective of the new design
(1) retain the colour scheme ideally to retain the brand identity, as have been using these colours since 2005.
(2) introduce more of my personality and make it more visually and overt that it is "Colin Ashworth's Notes for Wanderers", so possibly introducing my image into the blog banner so visitors are clear and more aware of the person behind the brand.
(3) needs to have an up-market, luxury but modern feel.
(4) if possible reflect the focus on the content (destinations, transportation, accommodation, attractions and journeys) - but this maybe best left to just words as want the design to be bold and more of the branding and personality.
Ideal wording
Smallish: Colin Ashworth's
Main wording: Notes for Wanderers
Sub-title/ small: luxurious destinations, transportation, accommodation and journeys.
Updates
I have a poll running with readers of my blog to rate the designs to help me to chose the final route, and so there is no need to submit any more designs. I will make the decision once the poll closes on the weekend.

```html
<!DOCTYPE html>
<html lang="en">
<head>
<meta charset="utf-8">
<title>About – Notes for Wanderers</title>
<link href="https://fonts.googleapis.com/css2?family=Open+Sans:wght@300;400;600;700&display=swap" rel="stylesheet">
<style>
  :root {
    --page: #ffffff;
    --ink: #3d3d3d;
    --nav-ink: #222222;
    --band-grey: #b9b9b9;
    --band-grey-light: #c9c9c9;
    --bubble: #231f20;
    --orange: #f7941d;
    --purple: #6a2c91;
    --purple-deep: #5b2487;
    --yellow: #fff200;
    --divider: #e3e3e3;
    --fb: #8fa5cf;
    --tw: #b6e6f2;
    --yt: #d9867d;
  }
  * { box-sizing: border-box; margin: 0; padding: 0; }
  html, body { width: 1200px; height: 1000px; overflow: hidden; background: var(--page); }
  body { position: relative; font-family: "Open Sans", Arial, sans-serif; color: var(--ink); }

  .banner { position: absolute; left: 21px; top: 159px; width: 1155px; height: 162px; overflow: hidden;
    background: linear-gradient(to bottom, var(--orange) 0%, #f9b868 38%, #ffffff 52%, var(--purple) 58%, var(--purple-deep) 100%); }
  .banner-city { position: absolute; left: 0; top: 0; width: 130px; height: 162px;
    background: linear-gradient(to bottom, #4a7fd0, #9cc0ea 55%, #3d6ab0); }
  .banner-portrait { position: absolute; left: 130px; top: 0; width: 205px; height: 162px;
    background: linear-gradient(to bottom, #f4a340 0%, #b5a9b8 40%, #3a3f55 100%); }
  .banner-beach { position: absolute; right: 0; top: 0; width: 236px; height: 162px;
    background: linear-gradient(to bottom, #3a63c6 0%, #8fb3e8 45%, #6fd0d8 70%, #efe7cf 100%); }
  .banner-bubble { position: absolute; left: 262px; top: 9px; width: 511px; height: 72px; border-radius: 30px;
    background: var(--bubble); display: flex; align-items: center; justify-content: center; padding: 0 28px; }
  .banner-title { font-weight: 700; font-size: 40px; line-height: 1; color: #fff; }
  .banner-owner { position: absolute; left: 314px; top: 96px; font-weight: 700; font-size: 36px; line-height: 1; color: #fff; }
  .banner-tagline { position: absolute; left: 660px; top: 90px; width: 470px;
    font-weight: 600; font-size: 21px; line-height: 30px; color: var(--yellow); }

  .site-frame { position: absolute; left: 24px; top: 321px; width: 1156px; height: 524px; overflow: hidden;
    border-left: 1px solid var(--divider); }

  .main-nav { position: absolute; right: 10px; top: 6px; display: flex; gap: 36px;
    font-weight: 300; font-size: 20px; color: var(--nav-ink); }
  .page-band { position: absolute; left: 0; top: 28px; width: 1156px; height: 85px;
    background: radial-gradient(ellipse at 50% 50%, var(--band-grey-light), var(--band-grey) 70%); }
  .page-title { position: absolute; left: 12px; top: 8px; font-weight: 300; font-size: 50px; color: #fff; }

  .content { position: absolute; left: 12px; top: 160px; width: 745px; font-size: 14px; line-height: 24px; letter-spacing: 0.35px; }
  .content p { margin-bottom: 24px; }
  .content strong { font-weight: 700; }
  .content-edge { position: absolute; left: 790px; top: 113px; width: 2px; height: 420px;
    box-shadow: 0 0 6px rgba(0,0,0,0.12); background: #f2f2f2; }

  .sidebar { position: absolute; left: 822px; top: 158px; width: 320px; }
  .sidebar h2 { font-weight: 300; font-size: 27px; color: #444; margin-bottom: 16px; }
  .social { display: flex; gap: 14px; margin-bottom: 52px; }
  .social span { width: 36px; height: 36px; border-radius: 5px; }
  .social .s-fb { background: var(--fb); }
  .social .s-tw { background: var(--tw); }
  .social .s-yt { background: var(--yt); }
  .ad-slot { margin-left: 69px; margin-top: -6px; width: 188px; height: 200px;
    background: linear-gradient(to bottom, #0b1a8f 0%, #11154d 55%, #5a3a10 80%, #e2a030 100%); }
</style>
</head>
<body>
  <header class="banner">
    <div class="banner-city" role="img" aria-label="Photo of a Paris landmark with fountains under a blue sky"></div>
    <div class="banner-portrait" role="img" aria-label="Portrait photo of the blogger"></div>
    <div class="banner-beach" role="img" aria-label="Photo of a tropical beach with palm trees"></div>
    <div class="banner-bubble"><span class="banner-title">Notes for Wanderers</span></div>
    <div class="banner-owner">Colin Ashworth's</div>
    <div class="banner-tagline">Luxurious destinations, Transportation, Accommodation and Journeys.</div>
  </header>

  <div class="site-frame">
    <nav class="main-nav"><span>Home</span><span>About</span><span>Top 10s</span><span>Podcast</span></nav>
    <div class="page-band"><h1 class="page-title">About</h1></div>
    <div class="content-edge"></div>

    <main class="content">
      <p><strong>What is Notes For Wanderers about?</strong></p>
      <p>Notes for Wanderers Luxury Travel Blog And Podcast</p>
      <p>Notes for Wanderers provides inspiration, advice and tips about luxurious travel experiences, including destinations, transportation, accommodation, attractions and journeys, that you can read, listen to or watch.</p>
      <p>It is for travelers who have the budget to indulge in a luxurious travel experience, and are seeking inspiration and recommendations. They are interested in the hottest and must-see and do, rather than the unusual, off-the-beaten track and uncharted.</p>
      <p><strong>We focus on 5 main topic areas: destinations, transportation, accommodation, attractions and journeys.</strong></p>
      <p>Notes for Wanderers provides honest and useful information, features and reviews across media, video and guides</p>
    </main>

    <aside class="sidebar">
      <h2>Follow On:</h2>
      <div class="social"><span class="s-fb"></span><span class="s-tw"></span><span class="s-yt"></span></div>
      <h2>Support Our Advertiser</h2>
      <div class="ad-slot" role="img" aria-label="Advertiser photo of a lit resort building at night"></div>
    </aside>
  </div>
</body>
</html>
```